BW Law Firm Needs Sharp Letterhead

Our law firm recently selected a new logo through Pixelfair. Now we need a sharp Letterhead using the Letterhead.

Target Market(s)

Legal community, business clients

Industry/Entity Type

Law Firm

Requirements
Must have
• Our Logo
• Gordon P. Ashby
• Board Certified
• Civil Trial Law
• Ohio Council of Counsel Accreditation
• gashby@bwlegalteam.com
• 2715-C West 6th
• McAllen, TX 78599
• 555-213-0476
• www.bwlegalteam.com

```html
<!DOCTYPE html>
<html lang="en">
<head>
<meta charset="utf-8">
<title>Brightwell Ashby Letterhead</title>
<link href="https://fonts.googleapis.com/css2?family=Marcellus+SC&display=swap" rel="stylesheet">
<style>
  :root {
    --paper: #ffffff;
    --ink: #141414;
    --grey: #6b6b6b;
    --band: #6e6e6e;
    --band-text: #f4f4f4;
    --mark-dark: #050505;
  }
  html, body {
    margin: 0;
    padding: 0;
    width: 961px;
    height: 1200px;
    overflow: hidden;
    background: var(--paper);
  }
  .letterhead {
    position: relative;
    width: 961px;
    height: 1200px;
    background: var(--paper);
    font-family: "Marcellus SC", "Times New Roman", serif;
  }
  .brand {
    position: absolute;
    top: 40px;
    left: 0;
    right: 0;
    display: flex;
    justify-content: center;
    align-items: center;
    gap: 10px;
  }
  .brand-square {
    width: 52px;
    height: 52px;
    background: var(--grey);
  }
  .brand-text {
    display: flex;
    flex-direction: column;
  }
  .brand-name {
    font-size: 34px;
    line-height: 1;
    color: var(--ink);
    letter-spacing: 0.5px;
    padding-bottom: 3px;
    border-bottom: 1px solid #9a9a9a;
  }
  .brand-tagline {
    font-size: 14.5px;
    color: var(--grey);
    letter-spacing: 0.6px;
    margin-top: 2px;
  }
  .attorney {
    position: absolute;
    top: 112px;
    left: 0;
    right: 0;
    text-align: center;
    color: var(--grey);
    font-size: 12px;
    line-height: 17px;
    letter-spacing: 0.4px;
  }
  .attorney .attorney-name {
    color: var(--ink);
    font-size: 14px;
  }
  .footer-band {
    position: absolute;
    left: 0;
    right: 0;
    bottom: 0;
    height: 84px;
    background: var(--band);
    color: var(--band-text);
    font-size: 13px;
  }
  .contact-list {
    position: absolute;
    left: 24px;
    top: 12px;
    margin: 0;
    padding: 0;
    list-style: none;
    line-height: 21px;
  }
  .contact-list li, .office .phone {
    display: flex;
    align-items: center;
    gap: 6px;
  }
  .contact-list svg, .office svg {
    width: 12px;
    height: 12px;
    fill: var(--band-text);
    flex: none;
  }
  .office {
    position: absolute;
    right: 22px;
    top: 12px;
    text-align: right;
    line-height: 17px;
  }
  .office .phone {
    justify-content: flex-end;
    margin-bottom: 8px;
  }
  .footer-mark {
    position: absolute;
    z-index: 2;
    left: 405px;
    top: 1032px;
    width: 151px;
    height: 132px;
    background: var(--paper);
    border-radius: 4px;
    padding: 0 14px 14px;
    box-sizing: border-box;
  }
  .footer-mark span {
    display: block;
    width: 100%;
    height: 100%;
    background: var(--mark-dark);
    border-radius: 2px;
  }
</style>
</head>
<body>
<main class="letterhead">
  <header class="brand">
    <div class="brand-square"></div>
    <div class="brand-text">
      <div class="brand-name">Brightwell Ashby</div>
      <div class="brand-tagline">Attorneys and Counselors</div>
    </div>
  </header>

  <section class="attorney">
    <div class="attorney-name">Gordon P. Ashby</div>
    <div>Board Certified &middot; Civil Trial Law</div>
    <div>Ohio Council of Counsel Accreditation</div>
  </section>

  <div class="footer-mark"><span></span></div>

  <footer class="footer-band">
    <ul class="contact-list">
      <li>
        <svg viewBox="0 0 16 16" aria-hidden="true"><path d="M3 7l1.5-4h7L13 7h1v5h-2v2h-2v-2H6v2H4v-2H2V7z M5 5.5L4.5 7h7L11 5.5z"/></svg>
        555-213-0476
      </li>
      <li>
        <svg viewBox="0 0 16 16" aria-hidden="true"><path d="M1 6l7-4 7 4v8H1z M3 7l5 3 5-3v-.5L8 4 3 6.5z"/></svg>
        gashby@bwlegalteam.com
      </li>
      <li>
        <svg viewBox="0 0 16 16" aria-hidden="true"><path d="M8 1a7 7 0 100 14A7 7 0 008 1zm0 1.5c.8 0 1.7 1.6 2 4H6c.3-2.4 1.2-4 2-4zM2.6 7h2.4c0 .7 0 1.4.1 2H2.6a5.5 5.5 0 010-2zm8.4 0h2.4a5.5 5.5 0 010 2H11c.1-.6.1-1.3 0-2zM6 9.5h4c-.3 2.4-1.2 4-2 4s-1.7-1.6-2-4z"/></svg>
        www.bwlegalteam.com
      </li>
    </ul>
    <div class="office">
      <div class="phone">
        <svg viewBox="0 0 16 16" aria-hidden="true"><path d="M4 1.5l2.5 3-1.5 1.5c.8 2 2.5 3.7 4.5 4.5L11 9l3 2.5-1.5 2.5C7 14 2 9 2 3.5z"/></svg>
        555-213-0476
      </div>
      <div>2715-C West 6th</div>
      <div>McAllen, TX 78599</div>
    </div>
  </footer>
</main>
</body>
</html>
```